Harbor Portable Scanning business cards / stationary
President CEO
Harbor Portable Scanning business cards / stationary - Health
Creative Brief
Professional
Lena Marcovici
P.O. Box 527 Ashwick NJ 08176
Info@harborportablescanninginc.com
www.harborportablescanninginc.com
I need business cards and stationary
I would like to see a version with my logo also on the back

```html
<!DOCTYPE html>
<html lang="en">
<head>
<meta charset="utf-8">
<title>Harbor Portable Scanning – Business Cards &amp; Stationery</title>
<link rel="stylesheet" href="https://fonts.googleapis.com/css2?family=Open+Sans:wght@400;600;700&display=swap">
<style>
  :root {
    --bg: #ece9e4;
    --paper: #ffffff;
    --brand-blue: #1f6fb2;
    --brand-sky: #5bc0eb;
    --brand-pale: #bfe6f7;
    --text-dark: #3a3f45;
    --card-grey-1: #f4f4f4;
    --card-grey-2: #d9d9d9;
    --line: #c9ced3;
  }
  * { box-sizing: border-box; margin: 0; padding: 0; }
  html, body { width: 1200px; height: 846px; overflow: hidden; }
  body {
    background: var(--bg);
    font-family: "Open Sans", Arial, sans-serif;
    color: var(--text-dark);
    position: relative;
  }
  .sheet {
    position: absolute;
    background: var(--paper);
    box-shadow: 0 3px 10px rgba(0,0,0,.18);
    overflow: hidden;
  }

  /* Plain footer bands */
  .bands { position: absolute; left: 0; right: 0; bottom: 0; display: flex; flex-direction: column; }
  .band-pale { background: var(--brand-pale); }
  .band-sky { background: var(--brand-sky); }
  .band-blue { background: var(--brand-blue); }

  .brand { display: flex; align-items: center; gap: 10px; }
  .brand-dot {
    border-radius: 50%;
    border: 3px solid var(--brand-sky);
    flex: none;
  }
  .brand-name {
    color: var(--brand-blue);
    font-weight: 600;
    letter-spacing: .06em;
    line-height: 1.15;
    text-transform: uppercase;
  }

  .contact { font-size: 9px; line-height: 1.55; text-align: right; }
  .contact b { color: var(--brand-blue); font-weight: 700; }
  .web { position: absolute; font-size: 10px; color: var(--text-dark); z-index: 2; }

  /* Letterhead */
  .letterhead { left: 252px; top: 40px; width: 700px; height: 776px; }
  .letterhead .brand { position: absolute; left: 46px; top: 56px; }
  .letterhead .brand-dot { width: 44px; height: 44px; }
  .letterhead .brand-name { font-size: 17px; width: 170px; }
  .letterhead .contact { position: absolute; right: 46px; top: 46px; }
  .letterhead .band-pale { height: 16px; }
  .letterhead .band-sky { height: 16px; }
  .letterhead .band-blue { height: 30px; }
  .letterhead .web { left: 0; right: 0; bottom: 10px; text-align: center; color: #fff; }

  /* Envelope */
  .envelope { left: 533px; top: 362px; width: 636px; height: 352px; }
  .envelope .flap { position: absolute; inset: 0; }
  .envelope .brand { position: absolute; left: 30px; top: 120px; }
  .envelope .brand-dot { width: 40px; height: 40px; }
  .envelope .brand-name { font-size: 15px; width: 160px; }
  .envelope .contact { position: absolute; left: 30px; top: 250px; text-align: left; }
  .envelope .band-pale { height: 10px; }
  .envelope .band-sky { height: 10px; }
  .envelope .band-blue { height: 16px; }
  .envelope .web { right: 30px; bottom: 60px; color: var(--brand-blue); }

  /* Business cards */
  .card { width: 336px; height: 196px; left: 60px; }
  .card-front { top: 174px; }
  .card-front .holder {
    position: absolute; right: 18px; top: 18px;
    font-size: 12px; font-weight: 700; color: var(--brand-blue);
  }
  .card-front .brand { position: absolute; left: 18px; top: 42px; }
  .card-front .brand-dot { width: 36px; height: 36px; }
  .card-front .brand-name { font-size: 12px; width: 120px; }
  .card-front .contact { position: absolute; right: 18px; top: 84px; font-size: 8px; }
  .card-front .band-pale { height: 6px; }
  .card-front .band-sky { height: 6px; }
  .card-front .band-blue { height: 12px; }
  .card-front .web { left: 0; right: 0; bottom: 40px; text-align: center; font-size: 9px; }

  .card-back {
    top: 394px;
    background: radial-gradient(circle at 50% 45%, var(--card-grey-1), var(--card-grey-2));
  }
  .card-back .brand { position: absolute; left: 0; right: 0; top: 56px; justify-content: center; }
  .card-back .brand-dot { width: 36px; height: 36px; }
  .card-back .brand-name { font-size: 12px; width: 120px; }
  .card-back .web {
    left: 0; right: 0; bottom: 38px; text-align: center;
    font-size: 10px; font-weight: 700; color: var(--text-dark);
  }
</style>
</head>
<body>

<section class="sheet letterhead">
  <div class="brand">
    <span class="brand-dot"></span>
    <span class="brand-name">Harbor Portable Scanning</span>
  </div>
  <div class="contact">
    P.O. Box 527<br>
    Ashwick NJ 08176<br>
    <b>Phone</b> : 856-555-0142<br>
    <b>Email</b> : Info@harborportablescanninginc.com
  </div>
  <div class="bands" aria-hidden="true">
    <div class="band-pale"></div>
    <div class="band-sky"></div>
    <div class="band-blue"></div>
  </div>
  <div class="web">www.harborportablescanninginc.com</div>
</section>

<section class="sheet envelope">
  <svg class="flap" viewBox="0 0 636 352" preserveAspectRatio="none" aria-hidden="true">
    <path d="M0 0 L318 110 L636 0" fill="none" stroke="var(--line)" stroke-width="1.2"/>
  </svg>
  <div class="brand">
    <span class="brand-dot"></span>
    <span class="brand-name">Harbor Portable Scanning</span>
  </div>
  <div class="contact">
    P.O. Box 527<br>
    Ashwick NJ 08176<br>
    <b>Phone</b> : 856-555-0142<br>
    <b>Email</b> : Info@harborportablescanninginc.com
  </div>
  <div class="web">www.harborportablescanninginc.com</div>
  <div class="bands" aria-hidden="true">
    <div class="band-pale"></div>
    <div class="band-sky"></div>
    <div class="band-blue"></div>
  </div>
</section>

<section class="sheet card card-front">
  <div class="holder">Lena Marcovici</div>
  <div class="brand">
    <span class="brand-dot"></span>
    <span class="brand-name">Harbor Portable Scanning</span>
  </div>
  <div class="contact">
    P.O. Box 527<br>
    Ashwick NJ 08176<br>
    <b>Phone</b> : 856-555-0142<br>
    <b>Email</b> : Info@harborportablescanninginc.com
  </div>
  <div class="web">www.harborportablescanninginc.com</div>
  <div class="bands" aria-hidden="true">
    <div class="band-pale"></div>
    <div class="band-sky"></div>
    <div class="band-blue"></div>
  </div>
</section>

<section class="sheet card card-back">
  <div class="brand">
    <span class="brand-dot"></span>
    <span class="brand-name">Harbor Portable Scanning</span>
  </div>
  <div class="web">www.harborportablescanninginc.com</div>
</section>

</body>
</html>
```